Eco-friendly waste company needs flyer design to promote collections

We need a flyer to promote our new small item collection service, offering cheaper waste collections to customers who usually would not want to pay for our high-eco performance business (we are expensive compared to companies who dispose of their waste in less eco-friendly ways). This flyer needs to be professional, informational, and classy to appeal to corporate office-based customers. We want photos used where possible, not cartoon or illustrations of objects we collect. I will attach our logo in various designs, and am really open to design options. We have a website that is ourdated, uses cartoons etc, and this is not landing well with our customer base so we want to move away from that kind of design. I need an A5-sized flyer, double sided. Please ask me if you have any questions!
Hi all,
Thank you all so much for so many wonderful designs, I will be looking through all of these tomorrow with my CEO and then I will update the project status again.
Thanks!!
Kind regards,
Mira

Hi all,
Thanks!!
Kind regards,
Mira

```html
<!DOCTYPE html>
<html lang="en">
<head>
<meta charset="utf-8">
<title>Verdant Haul – Collections Flyer</title>
<link href="https://fonts.googleapis.com/css2?family=Poppins:wght@400;600&display=swap" rel="stylesheet">
<style>
  :root {
    --ink: #1d1d1b;
    --mint: #9fd6c4;
    --sky: #7dbde0;
    --periwinkle: #8aa6d2;
    --band-top: #0b73b8;
    --band-bottom: #0a3d8c;
    --stripe: #1d5fb0;
    --stripe-light: #4b92cf;
    --white: #ffffff;
  }
  html, body { margin: 0; padding: 0; overflow: hidden; background: #ffffff; }
  .flyer {
    position: relative;
    width: 846px;
    height: 1200px;
    overflow: hidden;
    background: var(--white);
    font-family: "Poppins", sans-serif;
    color: var(--ink);
  }
  .backdrop { position: absolute; inset: 0; width: 846px; height: 1200px; }

  .brand {
    position: absolute; left: 30px; top: 318px;
    display: flex; align-items: center; gap: 12px;
  }
  .brand-dot {
    width: 16px; height: 16px; border-radius: 50%;
    background: var(--ink);
  }
  .brand-name {
    margin: 0;
    font-weight: 400;
    font-size: 38px;
    line-height: 44px;
    color: var(--ink);
  }

  .hazard-list {
    position: absolute; left: 36px; top: 455px; width: 408px;
    text-align: center; font-size: 20.6px; line-height: 28.2px;
  }
  .hazard-list p { margin: 0; }

  .data-service {
    position: absolute; left: 456px; top: 345px; width: 386px;
    font-size: 20.6px; line-height: 28.2px;
  }
  .data-service h2 {
    margin: 0 0 9px; font-weight: 400; font-size: 19.6px; line-height: 28.2px;
    text-transform: uppercase;
  }
  .data-service p { margin: 0; }
  .data-service ul { margin: 0; padding: 0 0 0 24px; list-style: none; }
  .data-service li::before { content: "• "; }

  .closing {
    position: absolute; left: 43px; top: 1013px; width: 720px;
    text-align: center; color: var(--white); font-size: 20.6px; line-height: 28.2px;
  }
  .closing p { margin: 0 0 3px; }
</style>
</head>
<body>
<div class="flyer">
  <svg class="backdrop" viewBox="0 0 846 1200" xmlns="http://www.w3.org/2000/svg">
    <defs>
      <linearGradient id="tech-photo" x1="0" y1="0" x2="1" y2="1">
        <stop offset="0" stop-color="#c9d3dc"/>
        <stop offset="0.5" stop-color="#7d8a97"/>
        <stop offset="1" stop-color="#e9ecef"/>
      </linearGradient>
      <linearGradient id="skip-photo" x1="0" y1="0" x2="0" y2="1">
        <stop offset="0" stop-color="#c7b597"/>
        <stop offset="0.5" stop-color="#a9a49a"/>
        <stop offset="1" stop-color="#8e8a85"/>
      </linearGradient>
      <linearGradient id="blue-hex" x1="0" y1="0" x2="1" y2="0">
        <stop offset="0" stop-color="var(--sky)"/>
        <stop offset="1" stop-color="var(--periwinkle)"/>
      </linearGradient>
      <linearGradient id="band" x1="0" y1="0" x2="1" y2="1">
        <stop offset="0" stop-color="var(--band-top)"/>
        <stop offset="1" stop-color="var(--band-bottom)"/>
      </linearGradient>
    </defs>

    <polygon class="photo-tech" role="img" aria-label="Photo of discarded computer cards, cables and a plug"
      points="330,0 846,0 846,300 720,310 560,200 420,80" fill="url(#tech-photo)"/>
    <rect class="photo-skip" role="img" aria-label="Photo of a skip filled with cardboard waste"
      x="430" y="830" width="416" height="170" fill="url(#skip-photo)"/>

    <polygon class="stripe" points="108,0 130,0 300,95 285,100" fill="var(--stripe-light)" opacity="0.7"/>
    <polygon class="stripe" points="198,80 210,76 700,300 690,305" fill="var(--stripe)"/>
    <polygon class="stripe" points="308,122 345,104 640,255 600,265" fill="var(--stripe)"/>
    <polygon class="stripe" points="700,300 846,225 846,245 720,307" fill="var(--stripe-light)" opacity="0.8"/>

    <polygon class="hex-mint" points="463,318 816,318 846,366 846,880 463,880 303,628"
      fill="var(--mint)" opacity="0.92"/>
    <polygon class="hex-blue" points="63,418 413,418 591,700 413,983 63,983 -115,700"
      fill="url(#blue-hex)" opacity="0.85"/>

    <polygon class="closing-band" points="0,1012 18,990 737,990 846,1077 846,1200 0,1200" fill="url(#band)"/>
  </svg>

  <div class="brand">
    <span class="brand-dot"></span>
    <h1 class="brand-name">Verdant Haul</h1>
  </div>

  <section class="hazard-list">
    <p>Need to get rid of items which can’t<br>go in your normal bin?</p>
    <p>We collect the following hazardous<br>items:</p>
    <p>• Paint - £4 per litre</p>
    <p>• Fluorescent tubes and bulbs -<br>£4 each</p>
    <p>• Cooking oil / hydraulic oil /<br>hazardous liquids – from £5 per litre</p>
    <p>• TV / Computer monitors - £10<br>each</p>
    <p>• Batteries – from £5 per kilo<br>(depends on type)</p>
    <p>• Gas bottles &amp; fire extinguishers -<br>£35 each Fridges – £40 for a small<br>fridge, £125 for a commercial fridge,<br>£200 for an ammonia fridge each</p>
    <p>• Air conditioners - £30 each</p>
  </section>

  <section class="data-service">
    <h2>Need to securely destroy data<br>on your computer or server?</h2>
    <p>We can securely collect and wipe<br>your data-holding electrical items,<br>allowing for their safe reuse. Items<br>that fail the wiping process will be<br>securely shredded and recycled.<br>Items include:</p>
    <ul>
      <li>Computers</li>
      <li>Laptops</li>
      <li>Servers</li>
      <li>Routers</li>
      <li>Switches</li>
      <li>Mobile phones</li>
      <li>Landline phones</li>
      <li>Printers with memory</li>
      <li>Photocopiers with memory</li>
    </ul>
  </section>

  <section class="closing">
    <p>We can provide certificates confirming data secure destruction,<br>either through securing wiping and reuse, or through shredding and<br>recycling.</p>
    <p>We can also securely destroy any paper, files, documents etc with<br>our shredding service.</p>
  </section>
</div>
</body>
</html>
```